new roofing company card

New primary business card for roofing company.

Industry/Entity Type

Residential roofing/Specializing in Asphalt and Standing seam metal roofing

Contact Information for Business Card

Phone number is: 484 672 1058 Email: support@fennridgeroofworks.com website: www.fennridgeroofworks.com

Colors
EB3D1F
EC4F4E
F09395
F8D3D4
FCEDEE

```html
<!DOCTYPE html>
<html lang="en">
<head>
<meta charset="utf-8">
<title>Fennridge Roofworks – Business Card</title>
<link rel="stylesheet" href="https://fonts.googleapis.com/css2?family=EB+Garamond:wght@400;600&display=swap">
<style>
  :root {
    --page-bg: #e4e4e8;
    --card-bg: #f4f4f3;
    --brand-red: #b81e1a;
    --brand-black: #1c1c1c;
    --text-dark: #222222;
    --font-serif: "EB Garamond", Georgia, serif;
  }
  * { box-sizing: border-box; margin: 0; padding: 0; }
  html, body {
    width: 1200px; height: 900px; overflow: hidden;
    background: var(--page-bg);
    font-family: var(--font-serif);
    color: var(--text-dark);
  }
  .sheet {
    width: 1200px; height: 900px;
    display: flex; flex-direction: column;
    align-items: center; justify-content: center; gap: 48px;
  }
  .card {
    position: relative;
    width: 630px; height: 360px;
    background: var(--card-bg);
    box-shadow: 0 10px 28px rgba(0,0,0,.18);
    overflow: hidden;
  }
  .card__brand {
    position: absolute; top: 46px; right: 44px;
    display: flex; align-items: center; gap: 14px;
  }
  .card__brand-mark {
    width: 26px; height: 26px; background: var(--brand-red);
  }
  .card__brand-name {
    font-size: 34px; font-weight: 600; line-height: 1;
    letter-spacing: 1px; color: var(--brand-black);
    text-transform: uppercase;
  }
  .card__footer-bar {
    position: absolute; left: 0; right: 0; bottom: 0;
    height: 18px; background: var(--brand-black);
  }
  .card__web-tab {
    position: absolute; right: 0; bottom: 18px;
    width: 300px; height: 56px;
    background: var(--brand-red);
    border-top-left-radius: 26px;
    display: flex; align-items: center; justify-content: center;
  }
  .card__web {
    color: #ffffff; font-size: 20px; font-weight: 600; letter-spacing: .3px;
  }
  .card__body {
    position: absolute; left: 48px; bottom: 92px;
  }
  .person__name {
    color: var(--brand-red); font-size: 24px; font-weight: 600;
    text-transform: uppercase; line-height: 1.1;
  }
  .person__role { font-size: 20px; margin-bottom: 14px; }
  .contact-list { list-style: none; }
  .contact-list li {
    display: flex; align-items: center; gap: 10px;
    font-size: 20px; line-height: 1.45;
  }
  .contact-list svg { width: 16px; height: 16px; flex: none; }
  .services__title {
    color: var(--brand-red); font-size: 26px; font-weight: 600;
    margin-bottom: 8px;
  }
  .services__list { list-style: none; }
  .services__list li {
    display: flex; align-items: center; gap: 12px;
    font-size: 20px; line-height: 1.45;
  }
  .services__list li::before {
    content: ""; width: 9px; height: 9px; border-radius: 50%;
    background: var(--brand-red); flex: none;
  }
</style>
</head>
<body>
<main class="sheet">

  <section class="card card--front">
    <div class="card__brand">
      <span class="card__brand-mark"></span>
      <span class="card__brand-name">Fennridge Roofworks</span>
    </div>

    <div class="card__body">
      <p class="person__name">Dana Whitlow</p>
      <p class="person__role">Director</p>
      <ul class="contact-list">
        <li>
          <svg viewBox="0 0 16 16" aria-hidden="true"><path fill="#b81e1a" d="M3.6 1.2l2.3 2.6-1.3 1.9c.9 2 2.4 3.5 4.4 4.5l1.9-1.3 2.6 2.3-1.4 2.6C6.6 13.6 2.4 9.4 1.2 3z"/></svg>
          484 672 1058
        </li>
        <li>
          <svg viewBox="0 0 16 16" aria-hidden="true"><rect x="1" y="3" width="14" height="10" fill="#b81e1a"/><path d="M1.5 3.5L8 9l6.5-5.5" fill="none" stroke="#ffffff" stroke-width="1.3"/></svg>
          support@fennridgeroofworks.com
        </li>
      </ul>
    </div>

    <div class="card__web-tab"><span class="card__web">www.fennridgeroofworks.com</span></div>
    <div class="card__footer-bar"></div>
  </section>

  <section class="card card--back">
    <div class="card__brand">
      <span class="card__brand-mark"></span>
      <span class="card__brand-name">Fennridge Roofworks</span>
    </div>

    <div class="card__body">
      <h2 class="services__title">Our Services</h2>
      <ul class="services__list">
        <li>Residential Roofing</li>
        <li>Specializing In Asphalt And</li>
        <li>Standing Seam Metal Roofing</li>
      </ul>
    </div>

    <div class="card__web-tab"><span class="card__web">www.fennridgeroofworks.com</span></div>
    <div class="card__footer-bar"></div>
  </section>

</main>
</body>
</html>
```